Logo needed for business card

Velistra Pty Ltd is in the business of healthcare and ecommerce.

We own and manage pharmacies and online health ecomerce sites.

We provide ecommerce consultants for companies looking for an ecommerce business startegy.

Think of it as the umbrella under which several healthcare brands may sit.

When I think of Velistra, I visulaise slick black/metalic colours, so please stay away from the common blue and green colours that seem to be so popular in this field.

Target Market(s)

CEOs and COOs

Industry/Entity Type

Healthcare

Contact Information for Business Card

Delphine Okoro
Director
Velistra Pty Ltd
4/237 Kelburn Pde
Ashvale, NSW 2047

Requirements
Must have
• Design must have scope to be implemented on the company's website and letterheads etc.

```html
<!DOCTYPE html>
<html lang="en">
<head>
<meta charset="utf-8">
<title>Velistra Pty Ltd – Business Card</title>
<link href="https://fonts.googleapis.com/css2?family=Josefin+Sans:wght@300;400&display=swap" rel="stylesheet">
<style>
  :root {
    --card-black: #121212;
    --card-charcoal: #1a1a1a;
    --ink-white: #f2f2f2;
    --mark-silver: #e6e6e6;
    --mark-rim: #3c3c3c;
  }
  html, body {
    margin: 0;
    padding: 0;
    width: 1200px;
    height: 741px;
    overflow: hidden;
    background: var(--card-black);
  }
  .card {
    position: relative;
    width: 1200px;
    height: 741px;
    background: radial-gradient(ellipse at 50% 45%, var(--card-charcoal) 0%, var(--card-black) 75%);
    font-family: "Josefin Sans", sans-serif;
    color: var(--ink-white);
  }
  .contact {
    position: absolute;
    left: 86px;
    top: 204px;
  }
  .contact__name {
    margin: 0;
    font-size: 96px;
    font-weight: 300;
    letter-spacing: 3px;
    line-height: 1;
    white-space: nowrap;
  }
  .contact__role {
    margin: 12px 0 0 2px;
    font-size: 52px;
    font-weight: 300;
    letter-spacing: 2px;
    line-height: 1.1;
  }
  .contact__address {
    margin: 30px 0 0 2px;
    font-style: normal;
    font-size: 47px;
    font-weight: 300;
    letter-spacing: 2px;
    line-height: 54px;
    white-space: nowrap;
  }
  .brand {
    position: absolute;
    left: 806px;
    top: 227px;
    width: 302px;
    height: 302px;
    box-sizing: border-box;
    border-radius: 50%;
    background: var(--mark-silver);
    border: 6px solid var(--mark-rim);
    display: flex;
    align-items: center;
    justify-content: center;
  }
  .brand__name {
    font-size: 46px;
    font-weight: 300;
    letter-spacing: 3px;
    color: var(--card-black);
    padding-top: 6px;
  }
</style>
</head>
<body>
  <main class="card">
    <section class="contact">
      <h1 class="contact__name">Delphine Okoro</h1>
      <p class="contact__role">Director</p>
      <address class="contact__address">
        Velistra Pty Ltd<br>
        4/237 Kelburn Pde Ashvale,<br>
        NSW 2047
      </address>
    </section>
    <div class="brand">
      <div class="brand__name">Velistra</div>
    </div>
  </main>
</body>
</html>
```